Brightmoor Senior Living Marketing Brochure, Covid-19 Brochure, Introduction to our manager

We are a Senior Living Community that services Assisted living and memory care. We have a lot of New programs for Activities, Food recipes, therapy, family and resident interaction , covid free, and want to introduce this to the community and existing family members.

Target Market(s)

La Jolla and San Diego for Brightmoor Senior Living and Memory Care of La Jolla and For Brightmoor Senior Living and Memory Care of Tarzana , San Fernando valley, tarzana, Encino , Woodland Hills Sherman oaks

Industry/Entity Type

Assisted Living

Colors
a54499
f7f3f9
ffffff
fece3e
ffc214

Requirements
Must have
• Product names for our marketing brochure , facility images per location

```html
<!DOCTYPE html>
<html lang="en">
<head>
<meta charset="utf-8">
<title>Brightmoor Senior Living Marketing Brochure</title>
<link rel="stylesheet" href="https://fonts.googleapis.com/css2?family=Bebas+Neue&family=Lato:wght@400;700&family=Roboto:wght@700;900&display=swap">
<style>
  :root{
    --purple:#a54499;
    --purple-deep:#8e3584;
    --lilac:#f7f3f9;
    --white:#ffffff;
    --gold:#ffc214;
    --gold-soft:#fece3e;
    --gold-deep:#e9aa0c;
    --ink:#111111;
    --stage:#4a4a4a;
  }
  *{box-sizing:border-box;margin:0;padding:0}
  html,body{width:1200px;height:1200px;overflow:hidden;background:var(--stage)}
  .stage{position:absolute;left:0;top:0;width:1500px;height:1500px;transform:scale(.8);transform-origin:0 0}
  .page{position:absolute;background:var(--white);overflow:hidden;font-family:"Lato",sans-serif;color:var(--ink)}
  .page svg.backdrop{position:absolute;left:0;top:0}
  .abs{position:absolute}

  /* ---------- Salon flyer ---------- */
  .salon{left:72px;top:79px;width:663px;height:929px}
  .brand-name{left:26px;top:34px;font-size:34px;font-weight:400;letter-spacing:-1px;color:var(--ink)}
  .portrait{left:3px;top:266px;width:320px;height:320px;border-radius:50%;border:10px solid var(--white);
    background:radial-gradient(circle at 55% 40%,#e9ddd3 0%,#b9c7d6 45%,#2d5a55 80%);box-shadow:0 2px 6px rgba(0,0,0,.15)}
  .call{left:330px;top:378px;width:236px;text-align:center;font-family:"Bebas Neue",sans-serif;color:var(--white);line-height:1}
  .call .label{font-size:30px}
  .call .phone{font-size:40px;margin-top:2px}
  .headline{left:321px;top:494px;font-family:"Bebas Neue",sans-serif;font-size:46px;line-height:46px;color:var(--ink)}
  .headline-rule{left:321px;top:584px;width:73px;height:6px;background:var(--purple)}
  .ticks{list-style:none;font-size:19px;line-height:18px}
  .ticks li{position:relative;padding-left:24px;margin-bottom:18px}
  .ticks li::before{content:"";position:absolute;left:2px;top:1px;width:12px;height:6px;border-left:3px solid var(--purple);border-bottom:3px solid var(--purple);transform:rotate(-45deg)}
  .ticks-left{left:28px;top:615px;width:300px}
  .ticks-right{left:346px;top:611px;width:300px}
  .divider{left:331px;top:612px;width:1px;height:222px;background:#444}
  .footer{left:0;bottom:0;width:100%;height:80px;background:linear-gradient(120deg,var(--purple-deep),var(--purple) 50%,#b24fa6);
    color:var(--white);font-weight:700;font-size:17px;display:flex;align-items:center;justify-content:center}
  .salon .footer{padding-right:20px;padding-bottom:22px}

  /* ---------- Assessment flyer ---------- */
  .assess{left:789px;top:452px;width:665px;height:933px}
  .assess-title{left:28px;top:24px;font-family:"Roboto",sans-serif;font-weight:900;font-size:28px;line-height:31px;color:var(--white);letter-spacing:.3px}
  .assess-rule{left:28px;top:86px;width:75px;height:5px;background:var(--white)}
  .dots{list-style:none;color:var(--white);font-size:15px;line-height:16px}
  .dots li{position:relative;padding-left:14px;margin-bottom:8px}
  .dots li::before{content:"";position:absolute;left:0;top:5px;width:5px;height:5px;border-radius:50%;background:var(--gold)}
  .dots-left{left:40px;top:107px;width:260px}
  .dots-right{left:334px;top:105px;width:310px;line-height:18px}
  .dots-right li{margin-bottom:14px}
  .feature{top:618px;width:210px;text-align:center}
  .feature h3{font-family:"Lato",sans-serif;font-weight:700;font-size:21px;line-height:25px;color:var(--purple)}
  .feature p{margin-top:10px;font-size:15px;line-height:18.3px}
  .feature-one{left:9px}
  .feature-two{left:230px;top:624px}
  .feature-three{left:448px;top:622px}
  .assess .footer{height:80px;padding-right:30px;padding-bottom:20px}
</style>
</head>
<body>
<div class="stage">

  <section class="page salon">
    <svg class="backdrop" width="663" height="929" viewBox="0 0 663 929" aria-hidden="true">
      <defs>
        <linearGradient id="salonGold" x1="0" y1="0" x2="1" y2="1">
          <stop offset="0" stop-color="var(--gold-soft)"/>
          <stop offset="1" stop-color="var(--gold-deep)"/>
        </linearGradient>
        <linearGradient id="salonRoom" x1="0" y1="0" x2="0" y2="1">
          <stop offset="0" stop-color="#f4f5f6"/>
          <stop offset=".55" stop-color="#d9dcdf"/>
          <stop offset="1" stop-color="#8e9196"/>
        </linearGradient>
      </defs>
      <path d="M0,268 Q330,420 663,118 V368 Q560,470 320,488 L0,488 Z" fill="url(#salonGold)"/>
      <path d="M0,0 H663 V130 Q560,300 400,370 Q200,410 0,280 Z" fill="url(#salonRoom)" role="img" aria-label="Photo of a bright salon interior with styling chairs"/>
    </svg>
    <div class="abs brand-name">Logo</div>
    <div class="abs portrait" role="img" aria-label="Photo of a smiling housekeeper holding folded white towels"></div>
    <div class="abs call"><div class="label">Call us @</div><div class="phone">123 456 7890</div></div>
    <h1 class="abs headline">Salon for nails hair<br>and massages :</h1>
    <div class="abs headline-rule"></div>
    <ul class="abs ticks ticks-left">
      <li>Housekeeping And Laundry Services</li>
      <li>Emergency Alert System</li>
      <li>Daily Activity Schedule</li>
      <li>Beauty Salon And Barber Shop</li>
      <li>Luxury Transportation: Meridian Shuttle Vans and Harbor Voyager Vans And Valet Services</li>
    </ul>
    <div class="abs divider"></div>
    <ul class="abs ticks ticks-right">
      <li>General Store</li>
      <li>Skyline TV Premium Package – Premium Sports Package, Vista Max, ReelTime And More!</li>
      <li>Movie Theatre, Shuffle Board, Pool Table And Outdoor BBQ</li>
      <li>Virtual Reality Station</li>
    </ul>
    <div class="abs footer">www.companyname..com</div>
  </section>

  <section class="page assess">
    <svg class="backdrop" width="665" height="933" viewBox="0 0 665 933" aria-hidden="true">
      <defs>
        <linearGradient id="assessGold" x1="0" y1="0" x2="1" y2="0">
          <stop offset="0" stop-color="var(--gold-deep)"/>
          <stop offset=".5" stop-color="var(--gold)"/>
          <stop offset="1" stop-color="var(--gold-deep)"/>
        </linearGradient>
        <linearGradient id="assessPurple" x1="0" y1="0" x2="1" y2="1">
          <stop offset="0" stop-color="#b04ea5"/>
          <stop offset=".6" stop-color="var(--purple)"/>
          <stop offset="1" stop-color="#b95aae"/>
        </linearGradient>
      </defs>
      <path d="M0,0 H665 V372 Q600,560 330,586 Q110,580 0,426 Z" fill="url(#assessGold)"/>
      <path d="M0,0 H665 V392 Q590,545 330,566 Q110,560 0,430 Z" fill="url(#assessPurple)" role="img" aria-label="Purple-tinted photo of a salon interior"/>
    </svg>
    <h2 class="abs assess-title">Multiple Resident Assessments Based<br>on Service Types</h2>
    <div class="abs assess-rule"></div>
    <ul class="abs dots dots-left">
      <li>Resident Task Scheduling and Service Plans</li>
      <li>End of Shift Reporting</li>
      <li>Resident Care Threads</li>
      <li>Resident Focus Areas and Incident Tracking and Reporting</li>
      <li>Meaningful and Customizable Dashboards</li>
      <li>Availability of standardized Focus Areas and Follow up Protocols</li>
      <li>Cost of Care Variance Reporting</li>
      <li>Customized Assessments (based on flexible points, time, or flat rate)</li>
      <li>eMAR</li>
      <li>Acuity Analysis</li>
      <li>State Forms and Reporting</li>
    </ul>
    <ul class="abs dots dots-right">
      <li>Scheduled care (includes non-assessment related tasks such as physician visits, TB testing, etc.)</li>
      <li>Acuity levels</li>
      <li>Staffing needs analysis for your Assisted Living, Memory Care or CCRC community is based on up-to-date resident assessments.</li>
      <li>Document resident risks, past incidents, individual behaviors, preferences, and additional family and caregiver input.</li>
      <li>Family and Resident Portal</li>
      <li>Brightmoor Senior Living is overcoming social isolation through the power of virtual reality and shared experiences.</li>
    </ul>
    <div class="abs feature feature-one">
      <h3>Living<br>Relive</h3>
      <p>Customized reminiscence therapy tools allow your residents to take a stroll down memory lane by revisiting their childhood home, wedding location or anywhere else from their past.</p>
    </div>
    <div class="abs feature feature-two">
      <h3>Connect<br>Reconnect</h3>
      <p>Customized reminiscence therapy tools allow your residents to take a stroll down memory lane by revisiting their childhood home, wedding location or anywhere else from their past.</p>
    </div>
    <div class="abs feature feature-three">
      <h3>Lightbulb<br>Reinspire</h3>
      <p>Create new friendships through the power of shared experience, all while providing unforgettable moments and stories that residents and their families will remember forever.</p>
    </div>
    <div class="abs footer">www.companyname..com</div>
  </section>

</div>
</body>
</html>
```